Redesign digital storytelling app interface for picking topics and recording/listening to audio

We are building an app for users to tell stories to their friends and family in response to prompts. Our current interface is very basic, and we want to have it redesigned in order to make it more visually appealing and feel more like a comfortable conversation. We also need one screen created from scratch to match the existing screens.
In this app, the user picks a story topic from a list a friend has sent to them and then makes an audio recording in response to that topic. The other user receives the recording and listens to it, then responds to the story.
Attached are images of the screens we want to have redesigned.
1. Topic Selection Screen - screen showing the three prompts that the user will pick from before recording their story.
2. Story Recording Screen - screen that the user sees while recording their story.
3. Playback Screen - screen that the user sees while listening to the story.
4. Respond to Story Screen - screen that the user sees after listening to the story on the playback screen. This screen should have buttons for the user to communicate with the person who sent them the story, including: a quick record button where the user can send a voice message responding to the story, a phone call button, a text button, a chatterlane button, and a vidoru button. It should also have a button to return to the main menu.
I've also attached a graphic showing what we are currently using for a logo and color scheme. This does not need to be followed exactly.
As an added bonus, please give an example of how to manage these screens when the stories are not one-on-one, but in a group of four people.
The mood of this product should be comfortable, personal, and conversational. We want people to feel like they're chatting with an old friend. The design itself can be anything at all, so go wild!

```html
<!DOCTYPE html>
<html lang="en">
<head>
<meta charset="utf-8">
<title>Talewick – Tell a Story</title>
<link href="https://fonts.googleapis.com/css2?family=Open+Sans:wght@300;400;600;700&display=swap" rel="stylesheet">
<style>
:root{
  --canvas-bg:#5f6163;
  --screen-bg:#ffffff;
  --status-bg:#000000;
  --brand-green:#56a12d;
  --ink:#1c1c1c;
  --muted:#c4c4c4;
  --track:#cfcfcf;
  --record-red:#ee1111;
  --icon-dark:#222222;
}
*{margin:0;padding:0;box-sizing:border-box}
html,body{width:960px;height:1200px;overflow:hidden;background:var(--canvas-bg);font-family:"Open Sans",Arial,sans-serif}
.screen{position:absolute;left:148px;top:12px;width:510px;height:905px;background:var(--screen-bg);transform:scale(1.3);transform-origin:0 0;overflow:hidden}
.status-bar{position:absolute;left:0;top:0;width:510px;height:33px;background:var(--status-bg);color:#fff;font-size:18px;font-weight:600}
.status-bar .signal{position:absolute;left:9px;top:9px}
.status-bar .clock{position:absolute;left:0;width:510px;text-align:center;top:5px}
.status-bar .battery{position:absolute;right:10px;top:5px;font-weight:400;display:flex;align-items:center;gap:5px}
.app-bar{position:absolute;left:0;top:33px;width:510px;height:49px;background:var(--brand-green);color:#fff}
.app-bar .title{position:absolute;left:0;width:510px;text-align:center;top:11px;font-size:18px;font-weight:700}
.app-bar .back{position:absolute;left:8px;top:12px}
.app-bar .brand{position:absolute;right:12px;top:14px;font-size:14px;font-weight:600}
.prompt{position:absolute;left:16px;top:104px;width:480px}
.avatar{position:absolute;left:0;top:0;width:100px;height:100px;border-radius:50%;background:radial-gradient(circle at 50% 45%,#c89a84,#6d5a50 70%,#3c3533)}
.prompt .asker{position:absolute;left:115px;top:14px;font-size:18px;color:var(--ink);font-weight:400}
.prompt .asker .name{color:var(--brand-green)}
.prompt .question{position:absolute;left:116px;top:44px;width:300px;font-size:18.5px;line-height:21px;color:var(--ink)}
.prompt .time{position:absolute;left:117px;top:89px;font-size:10px;color:var(--muted);display:flex;align-items:center;gap:3px}
.timer{position:absolute;left:0;width:510px;text-align:center;top:288px;font-size:58px;font-weight:400;color:var(--brand-green);letter-spacing:1px}
.state{position:absolute;left:0;width:510px;text-align:center;top:362px;font-size:28px;font-weight:300;color:var(--muted)}
.progress{position:absolute;left:58px;top:432px;width:394px;height:4px;background:var(--track);border-radius:2px}
.progress .fill{width:313px;height:4px;background:var(--brand-green);border-radius:2px}
.controls{position:absolute;left:0;top:528px;width:510px;height:140px}
.controls svg{position:absolute}
.send-button{position:absolute;left:125px;top:717px;width:246px;height:62px;border-radius:31px;background:var(--brand-green);color:#fff;font-size:19px;font-weight:600;display:flex;align-items:center;justify-content:center;border:none}
</style>
</head>
<body>
<main class="screen">
  <div class="status-bar">
    <svg class="signal" width="56" height="14" viewBox="0 0 56 14"><g fill="#fff"><circle cx="6" cy="7" r="5"/><circle cx="17" cy="7" r="5"/><circle cx="28" cy="7" r="5"/><circle cx="39" cy="7" r="5"/><circle cx="50" cy="7" r="5"/></g></svg>
    <div class="clock">10:30 PM</div>
    <div class="battery">
      <svg width="20" height="16" viewBox="0 0 20 16"><g fill="none" stroke="#fff" stroke-width="2" stroke-linecap="round"><path d="M2 6a12 12 0 0 1 16 0"/><path d="M5 9.5a7.5 7.5 0 0 1 10 0"/></g><circle cx="10" cy="13" r="2" fill="#fff"/></svg>
      <span>100%</span>
      <svg width="40" height="16" viewBox="0 0 40 16"><rect x="1" y="1" width="35" height="14" rx="2" fill="#fff" stroke="#fff"/><rect x="37" y="5" width="2" height="6" fill="#fff"/></svg>
    </div>
  </div>
  <header class="app-bar">
    <svg class="back" width="28" height="24" viewBox="0 0 28 24"><path d="M25 12H4M12 3L3 12l9 9" fill="none" stroke="#fff" stroke-width="2.5" stroke-linecap="round" stroke-linejoin="round"/></svg>
    <h1 class="title">Tell a Story</h1>
    <span class="brand">Talewick</span>
  </header>
  <section class="prompt">
    <div class="avatar" role="img" aria-label="Profile photo of Daniel, the friend asking the question"></div>
    <p class="asker"><span class="name">Daniel</span> asks</p>
    <p class="question">Would you rather travel by plane, train or car?</p>
    <p class="time"><svg width="10" height="10" viewBox="0 0 10 10"><circle cx="5" cy="5" r="4" fill="none" stroke="#c4c4c4"/><path d="M5 2.5V5h2" fill="none" stroke="#c4c4c4"/></svg>9:12 AM</p>
  </section>
  <div class="timer">00.09</div>
  <div class="state">Recording</div>
  <div class="progress"><div class="fill"></div></div>
  <div class="controls">
    <svg style="left:66px;top:44px" width="58" height="58" viewBox="0 0 58 58"><path d="M16 17A21 21 0 1 1 9 35" fill="none" stroke="var(--icon-dark)" stroke-width="5" stroke-linecap="round"/><path d="M3 15l17-2-5 16z" fill="var(--icon-dark)"/></svg>
    <svg style="left:183px;top:0" width="144" height="144" viewBox="0 0 144 144"><defs><radialGradient id="knob" cx="50%" cy="45%" r="55%"><stop offset="0" stop-color="#ffffff"/><stop offset=".75" stop-color="#f2f2f2"/><stop offset="1" stop-color="#d7d7d7"/></radialGradient></defs><circle cx="72" cy="72" r="69" fill="url(#knob)" stroke="#dddddd"/><circle cx="72" cy="70" r="29" fill="var(--record-red)"/></svg>
    <svg style="left:386px;top:44px" width="44" height="52" viewBox="0 0 44 52"><path d="M2 2l40 24L2 50z" fill="var(--icon-dark)"/></svg>
  </div>
  <button class="send-button">Send Recording</button>
</main>
</body>
</html>
```